Lantern Reach Website

Looking for a website design that clearly and powerfully portrays our unique and effective indoor advertising billboards in our network.

Our Classic Billboards and Wall Boards are strategically placed in high traffic areas of restaurants, pubs, nightclubs, fitness clubs, colleges & universities, and sports facilities.

Lantern Reach Network is our new name. Our current site is www.brightpostmarketing.ca
with our focus being entirely on our Out-of-Home Media Networks.

New website address will be www.lanternreach.ca

We need the following sections:
HOME

PRODUCTS (Drop down menu)
-Classic Billboards
-Wall Boards

NETWORKS (Drop down menu)
-Resto-Bar
-Sports
-Campus
-Casino

FEATURES

CAMPAIGNS

BECOME A PARTNER

CONTACT

Please include social media functions on the homepage such as twitter/facebook/linkdin

We will be supplying content and photos as required.

Our plan is to have you submit the homepage design to start with, and then we can start judging which styles we like the best and can start narrowing our list.

As a second round, we would like to ask the "finalists" to submit a second page (another section of the website) and to see how consistent you are in terms of the look and feel you proposed for the homepage.

Attached is our new logo.

Target Market(s)

Small Business Owners, Advertising Agencies, Media Buyers, Marketing Managers

Industry/Entity Type

Media

Number of Pages Required

1 page

Font styles to use
Sans Serif

Requirements
Must have
• Our Unique Network offers advertising solutions that feature:
• Guaranteed Readership,100% Gender Specific, Frequency, and Captive Audience. Purchasing advertising space in our network are small to medium business owners and advertising agencies booking on behalf of their clients.
• Site must be professional and modern looking.

```html
<!DOCTYPE html>
<html lang="en">
<head>
<meta charset="utf-8">
<title>Lantern Reach Network</title>
<link href="https://fonts.googleapis.com/css2?family=Open+Sans:wght@400;600;700;800&display=swap" rel="stylesheet">
<style>
:root{
  --red:#c8142b;
  --red-deep:#b5121b;
  --dark:#2b2b2b;
  --charcoal:#3d3d3d;
  --text:#333;
  --muted:#555;
  --line:#e2e2e2;
  --footer:#2d2d2d;
  --social:#444;
}
*{margin:0;padding:0;box-sizing:border-box}
html,body{width:767px;height:1200px;overflow:hidden;background:#fff}
body{position:relative;font-family:'Open Sans',sans-serif;color:var(--text)}
.abs{position:absolute}
.brand{left:46px;top:22px;display:flex;align-items:center;gap:8px}
.brand-dot{width:26px;height:26px;border-radius:50%;background:var(--red)}
.brand-name{font-size:25px;font-weight:700;color:var(--red);letter-spacing:-.3px}
.top-social{right:44px;top:18px;display:flex;gap:13px}
.top-social span{width:22px;height:22px;border-radius:50%;background:var(--social);display:block}
.nav{left:0;top:76px;width:767px;height:26px;background:var(--red-deep);display:flex;justify-content:space-between;padding:0 72px 0 70px;align-items:center}
.nav a{color:#fff;text-decoration:none;font-size:9.6px;font-weight:700;letter-spacing:.2px;height:26px;line-height:26px;padding:0 9px}
.nav a.active{background:var(--charcoal)}
.hero{left:0;top:102px;width:767px;height:333px;background:linear-gradient(90deg,#8e8a86 0%,#c9c9cb 22%,#d6d8db 40%,#4a5672 58%,#2e3a5a 80%,#6d6c6a 100%)}
.hero h1{position:absolute;left:0;width:767px;top:120px;text-align:center;color:#fff;font-size:34px;font-weight:800;line-height:44px;text-shadow:0 2px 3px rgba(0,0,0,.45)}
.hero .cta{position:absolute;left:330px;top:218px;width:107px;height:29px;background:var(--red);color:#fff;font-size:13.5px;font-weight:700;text-align:center;line-height:29px;border-radius:2px}
.hero .arrow{position:absolute;top:143px}
.dots{position:absolute;top:309px;left:345px;display:flex;gap:10px}
.dots i{width:11px;height:11px;border-radius:50%;border:1.5px solid #fff;display:block}
.dots i.on{background:#fff}
.welcome{left:0;top:450px;width:767px;text-align:center}
.welcome .kicker{font-size:25px;color:var(--red);letter-spacing:1px;line-height:32px}
.welcome h2{font-size:25px;font-weight:700;color:var(--dark);letter-spacing:1.3px;line-height:32px}
.rule{height:2px;background:var(--red);width:48px;margin:6px auto 0}
.about{left:57px;top:529px;width:656px;font-size:8.6px;line-height:9.4px;color:var(--text)}
.about p{margin-bottom:9px}
.sec-title{left:0;width:767px;text-align:center;font-size:25px;font-weight:700;color:var(--dark);letter-spacing:1.3px}
.sec-title em{font-style:normal;color:var(--red)}
.sec-rule{height:2px;background:var(--dark);width:47px}
.offers-sub{left:0;top:702px;width:767px;text-align:center;font-size:8.6px;line-height:16px;color:var(--muted)}
.offer{top:768px;width:160px;text-align:center}
.offer .ico{width:42px;height:42px;border-radius:50%;background:var(--red);margin:0 auto;display:flex;align-items:center;justify-content:center}
.offer p{margin-top:12px;font-size:12px;font-weight:700;line-height:15px;letter-spacing:.6px;color:var(--dark)}
.field{border:1px solid var(--line);font-size:8.6px;color:#999;padding:6px 8px;height:24px}
.field b{color:var(--red)}
.btn{top:1107px;height:24px;color:#fff;font-size:10.5px;font-weight:700;text-align:center;line-height:24px;letter-spacing:.5px}
.office{left:528px;top:955px;width:200px}
.office h3{font-size:17.5px;font-weight:700;color:var(--red);letter-spacing:.8px}
.office h4{font-size:14px;font-weight:700;color:var(--dark);margin-top:9px;letter-spacing:.6px}
.office .addr{font-size:8px;line-height:10px;margin-top:8px;color:var(--text)}
.office .row{font-size:10px;margin-top:8px;color:var(--dark)}
.office .row b{font-weight:700}
.footer{left:0;top:1161px;width:767px;height:39px;background:var(--footer)}
.footer .copy{position:absolute;left:84px;top:13px;font-size:9.6px;color:#ddd}
.footer .soc{position:absolute;right:42px;top:9px;display:flex;gap:10px}
.footer .soc span{width:21px;height:21px;border-radius:50%;display:block}
</style>
</head>
<body>

<div class="abs brand"><span class="brand-dot"></span><span class="brand-name">Lantern Reach Network</span></div>
<div class="abs top-social" aria-label="Social links"><span></span><span></span><span></span></div>

<nav class="abs nav">
  <a>HOME</a><a>PRODUCTS</a><a class="active">NETWORKS ▾</a><a>FEATURES</a><a>CAMPAIGNS</a><a>BECOME A PARTNER</a><a>CONTACT</a>
</nav>

<section class="abs hero">
  <div role="img" aria-label="Indoor billboard in a tiled corridor showing a sports team advertisement" style="position:absolute;inset:0"></div>
  <svg class="arrow" style="left:26px" width="16" height="30" viewBox="0 0 16 30"><path d="M14 2 2 15l12 13" fill="none" stroke="#fff" stroke-width="2.5"/></svg>
  <svg class="arrow" style="left:722px" width="16" height="30" viewBox="0 0 16 30"><path d="M2 2l12 13L2 28" fill="none" stroke="#fff" stroke-width="2.5"/></svg>
  <h1>Over 1000 Billboards 3 Targeted<br>Networks Regional Coverage</h1>
  <div class="cta">KNOW MORE</div>
  <div class="dots"><i class="on"></i><i></i><i></i><i></i></div>
</section>

<section class="abs welcome">
  <div class="kicker">Welcome</div>
  <h2>Lantern Reach Network</h2>
  <div class="rule"></div>
</section>

<div class="abs about">
  <p>Established in 1996, Brightpost Advertising Network is a Canadian out-of-home media company based in Kamloops, British Columbia.</p>
  <p>Brightpost Advertising Network offers innovative and effective indoor Classic Billboards and Wallboards that are strategically placed in high traffic areas<br>&nbsp;of restaurants, pubs, nightclubs, fitness clubs, colleges and universities, and sports arenas.</p>
  <p>Brightpost Advertising Network offers high impact branding placements at high traffic properties throughout British Columbia.</p>
  <p>Brightpost Advertising Network also specializes in the area of developing long-term revenue streams through the selling of sponsorship, supplier partner-<br>ships and naming rights packages</p>
</div>

<h2 class="abs sec-title" style="top:653px">Our <em>Offers</em></h2>
<div class="abs sec-rule" style="left:361px;top:688px"></div>
<div class="abs offers-sub">Lorem Ipsum is simply dummy text type setting industry esse cillum dolore eu fugiat nulla pariatur.<br>Excepteur sint occaecat.</div>

<div class="abs offer" style="left:62px">
  <div class="ico"><svg width="22" height="24" viewBox="0 0 22 24" fill="none" stroke="#fff" stroke-width="2"><circle cx="11" cy="8" r="6"/><circle cx="11" cy="8" r="2.5"/><path d="M7 13l-3 9 4-2 2 3 1-8M15 13l3 9-4-2-2 3-1-8"/></svg></div>
  <p>Guaranteed<br>Readership</p>
</div>
<div class="abs offer" style="left:225px">
  <div class="ico"><svg width="24" height="24" viewBox="0 0 24 24" fill="none" stroke="#fff" stroke-width="2.2"><circle cx="10" cy="11" r="5"/><path d="M10 16v6M7 19h6M14 7l6-5M15 2h5v5"/></svg></div>
  <p>100% Gender<br>Specific</p>
</div>
<div class="abs offer" style="left:386px">
  <div class="ico"><svg width="24" height="20" viewBox="0 0 24 20" fill="none" stroke="#fff" stroke-width="2"><rect x="2" y="2" width="20" height="16" rx="1"/><path d="M2 6h20M5 15l4-4 3 2 4-4 4 4"/></svg></div>
  <p style="margin-top:19px">Frequency</p>
</div>
<div class="abs offer" style="left:548px">
  <div class="ico"><svg width="28" height="20" viewBox="0 0 28 20" fill="#fff"><circle cx="14" cy="5" r="4"/><circle cx="6" cy="7" r="3"/><circle cx="22" cy="7" r="3"/><path d="M7 19c0-5 3-8 7-8s7 3 7 8zM1 18c0-4 2-6 5-6 1 0 2 .3 2.5 .8-1.5 1.5-2.3 3-2.5 5.2zM27 18c0-4-2-6-5-6-1 0-2 .3-2.5 .8 1.5 1.5 2.3 3 2.5 5.2z"/></svg></div>
  <p>Captive<br>Audience</p>
</div>

<h2 class="abs sec-title" style="top:892px">Contact <em>Us</em></h2>
<div class="abs sec-rule" style="left:362px;top:927px"></div>

<form>
  <div class="abs field" style="left:84px;top:948px;width:210px">Your Name<b>*</b></div>
  <div class="abs field" style="left:298px;top:948px;width:211px">E-mail <b>*</b></div>
  <div class="abs field" style="left:84px;top:981px;width:210px">Phone</div>
  <div class="abs field" style="left:298px;top:981px;width:211px">Member Number</div>
  <div class="abs field" style="left:84px;top:1015px;width:425px;height:84px;padding-top:10px">Massage</div>
  <div class="abs btn" style="left:85px;width:207px;background:var(--red)">SUBMIT</div>
  <div class="abs btn" style="left:298px;width:210px;background:var(--charcoal)">CLEAR ALL</div>
</form>

<aside class="abs office">
  <h3>MAIN OFFICE</h3>
  <h4>Lantern Reach Network</h4>
  <div class="addr">Suite #210, 45 Harbour Lane<br>Kamloops, BC, V2C 0A0</div>
  <div class="row" style="margin-top:14px"><b>Phone:</b>&nbsp; 250.555.0148</div>
  <div class="row"><b>Email:</b> info@lanternreach.ca</div>
  <div class="row"><b>Mon - Fri 9am - 5pm EST</b></div>
</aside>

<footer class="abs footer">
  <div class="copy">Copyright © lanternreach.ca. All Rights Reserved.</div>
  <div class="soc" aria-label="Social links"><span style="background:#3b5998"></span><span style="background:#4a9fe0"></span><span style="background:#1f6fb2"></span><span style="background:#dc4a38"></span></div>
</footer>

</body>
</html>
```